Templates for Construction Company

We are looking to have templates prepared for all aspects of our letter sending. Using our brand design. with similar layouts that look the same.

Letterheads design & Email signatures

We use letter heads for - quotes, contract correspondence, variations, formal letters, invitations

Target Market(s)

Clients documents sent in emails

Industry/Entity Type

Construction

Font styles to use
Serif
Sans Serif

Colors
0054AA
0677BA
7BADD7
CADEEF
E8F1F8

Requirements
Must have
• Easy to read, water marks on page
Nice to have
• Different options for different letters

```html
<!DOCTYPE html>
<html lang="en">
<head>
<meta charset="utf-8">
<title>Stonefield Building Group – Letterhead &amp; Email Signature</title>
<link rel="stylesheet" href="https://fonts.googleapis.com/css2?family=Montserrat:wght@500;600;700&family=Roboto:wght@400;500;700&family=Pinyon+Script&display=swap">
<style>
  :root {
    --canvas: #e4e2e3;
    --paper: #f0f0f0;
    --brand-blue: #4f80c6;
    --deep-blue: #1f56a6;
    --ink: #1e1e1e;
    --label-grey: #555557;
    --footer-dark: #232323;
    --watermark: #cbdaeb;
    --shadow: rgba(0,0,0,0.35);
  }
  * { margin: 0; padding: 0; box-sizing: border-box; }
  html, body { width: 1200px; height: 619px; overflow: hidden; }
  body { background: var(--canvas); position: relative; font-family: "Roboto", sans-serif; color: var(--ink); }

  .section-label {
    position: absolute; font-family: "Montserrat", sans-serif; font-weight: 600;
    color: var(--label-grey); font-size: 18px; letter-spacing: 2.4px;
  }
  .section-label--letterhead { left: 29px; top: 36px; }
  .section-label--signature { left: 465px; top: 166px; }

  .brand-name {
    position: absolute; display: flex; align-items: center; gap: 6px;
    font-family: "Roboto", sans-serif; font-weight: 700; color: var(--brand-blue); line-height: 1;
  }
  .brand-name__square { background: var(--brand-blue); flex: none; }

  /* Letterhead */
  .letterhead {
    position: absolute; left: 30px; top: 67px; width: 399px; height: 512px;
    background: var(--paper); box-shadow: 4px 5px 8px var(--shadow); overflow: hidden;
  }
  .letterhead .brand-name { left: 26px; top: 30px; font-size: 17px; }
  .letterhead .brand-name__square { width: 16px; height: 36px; }
  .letterhead .brand-name__text { line-height: 1.05; }

  .contact-block {
    position: absolute; left: 277px; top: 19px; height: 56px;
    border-left: 1px solid var(--deep-blue); padding-left: 6px;
    font-size: 7px; line-height: 10px;
  }
  .contact-block__company { color: var(--deep-blue); font-weight: 500; }
  .contact-block__row { display: flex; align-items: center; gap: 7px; }
  .contact-block__address { margin-bottom: 5px; }
  .contact-icon { width: 8px; height: 8px; flex: none; }

  .watermark-name {
    position: absolute; font-family: "Roboto", sans-serif; font-weight: 700;
    color: var(--watermark); white-space: nowrap; line-height: 1;
  }
  .letterhead .watermark-name { left: 58px; top: 222px; font-size: 58px; opacity: 0.75; }

  .recipient {
    position: absolute; left: 26px; top: 131px;
    font-family: "Montserrat", sans-serif; font-weight: 700; font-size: 7.2px;
    letter-spacing: 0.7px; line-height: 9px;
  }
  .letter-body {
    position: absolute; left: 26px; top: 168px; width: 347px;
    font-family: "Montserrat", sans-serif; font-weight: 500; font-size: 8px;
    letter-spacing: 0.62px; line-height: 9.5px; text-align: justify;
  }
  .letter-body p { margin-bottom: 9.5px; }
  .sign-off { position: absolute; left: 25px; top: 360px; }
  .sign-off__signature { font-family: "Pinyon Script", cursive; font-size: 17px; line-height: 20px; }
  .sign-off__title { font-family: "Montserrat", sans-serif; font-weight: 500; font-size: 12px; letter-spacing: 1.1px; }

  .page-footer { position: absolute; left: 0; bottom: 0; }
  .page-footer__url {
    position: absolute; color: #fff; font-family: "Roboto", sans-serif; white-space: nowrap;
  }
  .letterhead .page-footer { width: 399px; height: 23px; }
  .letterhead .page-footer__url { left: 281px; top: 6px; font-size: 9px; }

  /* Email signature */
  .email-signature {
    position: absolute; left: 466px; top: 203px; width: 704px; height: 246px;
    background: var(--paper); box-shadow: 4px 5px 8px var(--shadow); overflow: hidden;
  }
  .email-signature .watermark-name { left: 368px; top: -18px; font-size: 104px; opacity: 0.85; }
  .email-signature .brand-name { left: 44px; top: 30px; font-size: 21px; }
  .email-signature .brand-name__square { width: 20px; height: 44px; }
  .email-signature .brand-name__text { line-height: 1.05; }

  .signature-details { position: absolute; left: 44px; top: 135px; font-size: 11px; line-height: 14.5px; }
  .signature-details__company { color: var(--deep-blue); font-weight: 500; }
  .signature-details__address { margin-bottom: 4px; }
  .signature-details__row { display: flex; align-items: center; gap: 11px; line-height: 16px; }
  .signature-details .contact-icon { width: 12px; height: 12px; }

  .email-signature .page-footer { width: 704px; height: 37px; }
  .email-signature .page-footer__url { left: 492px; top: 9px; font-size: 16.5px; }
</style>
</head>
<body>

<h2 class="section-label section-label--letterhead">Latterhead</h2>

<article class="letterhead">
  <div class="brand-name">
    <span class="brand-name__square"></span>
    <span class="brand-name__text">Stonefield<br>Building Group</span>
  </div>

  <address class="contact-block" style="font-style:normal">
    <div class="contact-block__company">Stonefield Building Group</div>
    <div class="contact-block__address">Your Address line<br>here, Harbourview 23560</div>
    <div class="contact-block__row">
      <svg class="contact-icon" viewBox="0 0 16 16" aria-hidden="true"><path d="M3 1.5l3 .5 1 3.5-2 1.5c1 2 2.5 3.5 4.5 4.5l1.5-2 3.5 1 .5 3c-6 1.5-13-5.5-12-12z" fill="var(--deep-blue)"/></svg>
      <span>+00 123 456 78</span>
    </div>
    <div class="contact-block__row">
      <svg class="contact-icon" viewBox="0 0 16 16" aria-hidden="true"><rect x="1" y="3.5" width="14" height="9" fill="var(--deep-blue)"/><path d="M1.5 4l6.5 5 6.5-5M1.5 12l5-4M14.5 12l-5-4" stroke="#fff" stroke-width="1" fill="none"/></svg>
      <span>yourname@mailbox.com</span>
    </div>
  </address>

  <div class="watermark-name" aria-hidden="true">Stonefield</div>

  <div class="recipient">TO<br>Rafiq Hossain<br>Northgate, Ridgeview</div>

  <div class="letter-body">
    <p>Lorem ipsum dolor sit amet, consectetur adipisicing elit, sed do eiusmod tempor incididunt ut labore et dolore magna aliqua. Ut enim ad minim veniam, quis nostrud exercitation ullamco laboris nisi ut aliquip ex ea commodo consequat. Duis aute irure dolor in reprehenderit</p>
    <p>in voluptate velit esse cillum dolore eu fugiat nulla pariatur. Excepteur sint occaecat cupidatat non proident, sunt in culpa qui officia deserunt mollit anim id est laborum. Sed ut perspiciatis unde omnis iste natus error sit voluptatem</p>
    <p>accusantium doloremque laudantium, totam rem aperiam, eaque ipsa quae ab illo inventore veritatis et quasi architecto beatae vitae dicta sunt explicabo. Nemo enim ipsam voluptatem quia voluptas sit aspernatur aut odit aut fugit, sed quia consequuntur magni dolores eos qui</p>
    <p>ratione voluptatem sequi nesciunt. Neque porro quisquam est, qui dolorem ipsum quia dolor sit amet, consectetur, adipisci velit, sed quia non numquam eius modiquaerat</p>
  </div>

  <div class="sign-off">
    <div class="sign-off__signature">Daniel Marsh</div>
    <div class="sign-off__title">President</div>
  </div>

  <footer class="page-footer">
    <svg width="399" height="23" viewBox="0 0 399 23" aria-hidden="true">
      <polygon points="0,12 256,12 252,23 0,23" fill="var(--deep-blue)"/>
      <polygon points="268,0 399,0 399,23 258,23" fill="var(--footer-dark)"/>
    </svg>
    <span class="page-footer__url">www.yourwebsite.com</span>
  </footer>
</article>

<h2 class="section-label section-label--signature">Email Signature</h2>

<section class="email-signature">
  <div class="watermark-name" aria-hidden="true">Stonefield</div>

  <div class="brand-name">
    <span class="brand-name__square"></span>
    <span class="brand-name__text">Stonefield<br>Building Group</span>
  </div>

  <div class="signature-details">
    <div class="signature-details__company">Stonefield Building Group</div>
    <div class="signature-details__address">Your Address line<br>here, Harbourview 23560</div>
    <div class="signature-details__row">
      <svg class="contact-icon" viewBox="0 0 16 16" aria-hidden="true"><path d="M3 1.5l3 .5 1 3.5-2 1.5c1 2 2.5 3.5 4.5 4.5l1.5-2 3.5 1 .5 3c-6 1.5-13-5.5-12-12z" fill="var(--deep-blue)"/></svg>
      <span>+00 123 456 78</span>
    </div>
    <div class="signature-details__row">
      <svg class="contact-icon" viewBox="0 0 16 16" aria-hidden="true"><rect x="1" y="3.5" width="14" height="9" fill="var(--deep-blue)"/><path d="M1.5 4l6.5 5 6.5-5M1.5 12l5-4M14.5 12l-5-4" stroke="#fff" stroke-width="1" fill="none"/></svg>
      <span>yourname@mailbox.com</span>
    </div>
  </div>

  <footer class="page-footer">
    <svg width="704" height="37" viewBox="0 0 704 37" aria-hidden="true">
      <polygon points="0,22 454,22 449,37 0,37" fill="var(--deep-blue)"/>
      <polygon points="470,0 704,0 704,37 455,37" fill="var(--footer-dark)"/>
    </svg>
    <span class="page-footer__url">www.yourwebsite.com</span>
  </footer>
</section>

</body>
</html>
```